Business card por a urban DJ, up scale audience target

Need a sober design, modern, conservative colors but i can consider some options, y play rnb, hip hop, EDM and top40.

Business card for contact and personal info, double sided, use logo attrached please; im 42 so i need a card acording to my age an target audience.

Target Market(s)

Adult people, up scale audience

Industry/Entity Type

Music Download

Contact Information for Business Card

Cel (318) 5024471963 www.kelvarodun.com

Requirements
Must have
• open mind
Nice to have
• open mind
Should not have
• DJ

```html
<!DOCTYPE html>
<html lang="en">
<head>
<meta charset="utf-8">
<title>Kelva — Business Card</title>
<link rel="stylesheet" href="https://fonts.googleapis.com/css2?family=Montserrat:wght@800&family=Open+Sans:wght@400&display=swap">
<style>
  :root {
    --backdrop: #c8c8c8;
    --ink: #1c1c1c;
    --paper: #f7f7f7;
    --logo-white: #ffffff;
    --detail-grey: #3a3a3a;
    --icon-grey: #555555;
  }
  * { margin: 0; padding: 0; box-sizing: border-box; }
  html, body {
    width: 1093px;
    height: 1200px;
    overflow: hidden;
    background: var(--backdrop);
  }
  .canvas {
    position: relative;
    width: 1093px;
    height: 1200px;
  }
  .card {
    position: absolute;
    left: 166px;
    width: 760px;
    height: 434px;
    border-radius: 32px;
    overflow: hidden;
  }
  .card--front {
    top: 130px;
    background: var(--ink);
    display: flex;
    align-items: center;
    justify-content: center;
  }
  .brand-name {
    font-family: "Montserrat", sans-serif;
    font-weight: 800;
    font-size: 110px;
    letter-spacing: 2px;
    color: var(--logo-white);
    line-height: 1;
  }
  .card--back {
    top: 636px;
    background: var(--paper);
  }
  .corner-accent {
    position: absolute;
    inset: 0;
    width: 100%;
    height: 100%;
  }
  .contact {
    position: absolute;
    left: 58px;
    top: 50px;
  }
  .contact__name {
    font-family: "Montserrat", sans-serif;
    font-weight: 800;
    font-size: 54px;
    letter-spacing: 1px;
    color: var(--ink);
    line-height: 1;
    margin-bottom: 18px;
  }
  .contact__line {
    display: flex;
    align-items: center;
    gap: 16px;
    font-family: "Open Sans", sans-serif;
    font-weight: 400;
    font-size: 28px;
    color: var(--detail-grey);
    line-height: 1.45;
  }
  .contact__icon {
    width: 18px;
    height: 18px;
    flex: none;
  }
  .contact__dot {
    width: 14px;
    height: 14px;
    margin: 0 2px;
    border-radius: 50%;
    background: var(--icon-grey);
    flex: none;
  }
</style>
</head>
<body>
<main class="canvas">
  <section class="card card--front" aria-label="Card front">
    <span class="brand-name">KELVA</span>
  </section>

  <section class="card card--back" aria-label="Card back">
    <svg class="corner-accent" viewBox="0 0 760 434" preserveAspectRatio="none" aria-hidden="true">
      <polygon points="470,434 760,170 760,434" fill="var(--ink)"/>
    </svg>
    <div class="contact">
      <h1 class="contact__name">JOHN DOE</h1>
      <p class="contact__line">
        <svg class="contact__icon" viewBox="0 0 24 24" aria-hidden="true">
          <path fill="var(--icon-grey)" d="M6.6 10.8a15.1 15.1 0 0 0 6.6 6.6l2.2-2.2a1 1 0 0 1 1-.25 11.4 11.4 0 0 0 3.6.57 1 1 0 0 1 1 1V20a1 1 0 0 1-1 1A17 17 0 0 1 3 4a1 1 0 0 1 1-1h3.5a1 1 0 0 1 1 1c0 1.25.2 2.45.57 3.6a1 1 0 0 1-.25 1z"/>
        </svg>
        <span>(318) 5024471963</span>
      </p>
      <p class="contact__line">
        <span class="contact__dot" aria-hidden="true"></span>
        <span>www.kelvarodun.com</span>
      </p>
    </div>
  </section>
</main>
</body>
</html>
```